Zielgruppe
Gesundheitsberatung
Aufgabenstellung
Es soll ein gutes, fröhliches Gefühl geben, die Visitenkarte anzuschauen, jedoch darf es auch nicht zu verspielt sein.
Farbiger Fond, bitte nicht,
Mitgeschickte Dateien geben einen Eindruck, was ich ganz gut finde, aber irgendwie wirkt es wie selbstgestaltet. Foto muss nicht verwendet werden. Ja/nein?
Vielleicht ist es besser mit der Figur zu spielen. Das Logo kann auch nur die Schrift mit der Subheadline sein. Schrift ist Calibri light - also easy
Farben sind gelb für das Leben
Blau für die Arbeit, Denken, Rationale.
Blautöne des Mänchens verwenden.
Texte unter Visitenkarte eigene Datei.

```html
<!DOCTYPE html>
<html lang="de">
<head>
<meta charset="utf-8">
<title>KraftQuellen – Visitenkarte</title>
<link href="https://fonts.googleapis.com/css2?family=Open+Sans:wght@300;400;600&display=swap" rel="stylesheet">
<style>
  :root {
    --blue: #0b5cb5;
    --blue-deep: #0a4f9e;
    --yellow: #ffda2e;
    --white: #ffffff;
    --ink: #1d1d1f;
    --backdrop: #e9e7e3;
  }
  html, body {
    margin: 0; padding: 0;
    width: 1200px; height: 822px;
    overflow: hidden;
    background: var(--backdrop);
    font-family: "Open Sans", Calibri, sans-serif;
  }
  .canvas { position: relative; width: 1200px; height: 822px; }
  .card {
    position: absolute;
    width: 560px; height: 320px;
    overflow: hidden;
    box-shadow: 0 6px 18px rgba(0,0,0,.18);
  }
  /* Rückseite */
  .card--back { left: 50px; top: 60px; background: var(--blue); color: var(--white); }
  .quote {
    position: absolute; left: 36px; top: 34px;
    font-size: 15px; line-height: 1.45; font-weight: 400; letter-spacing: .3px;
  }
  .quote__author { color: var(--yellow); font-size: 13px; margin-left: 18px; }
  .brand {
    position: absolute; left: 36px; top: 140px;
    display: flex; align-items: center; gap: 14px;
  }
  .brand__name { font-size: 46px; font-weight: 400; letter-spacing: .5px; line-height: 1; }
  .brand__dot { width: 22px; height: 22px; border-radius: 50%; background: var(--yellow); }
  .brand__tagline {
    position: absolute; left: 38px; top: 196px;
    font-size: 22px; font-weight: 300; letter-spacing: 1.5px;
  }
  .benefits {
    position: absolute; left: 36px; bottom: 30px;
    font-size: 15px; font-weight: 400; letter-spacing: .3px;
  }
  .sep { color: var(--yellow); margin: 0 6px; }

  /* Vorderseite */
  .card--front { left: 590px; top: 442px; background: var(--white); }
  .waves { position: absolute; inset: 0; }
  .person { position: absolute; left: 30px; top: 44px; color: var(--blue); }
  .person__name { font-size: 29px; font-weight: 400; margin: 0; line-height: 1.1; }
  .person__offer { font-size: 15px; font-weight: 400; line-height: 1.35; margin-top: 6px; }
  .credentials {
    position: absolute; left: 30px; top: 160px;
    color: var(--ink); font-size: 14px; line-height: 1.45;
  }
  .contact { position: absolute; left: 30px; top: 214px; color: var(--ink); font-size: 15px; line-height: 1.6; }
  .contact__row { display: flex; align-items: center; gap: 10px; }
  .contact__icon { width: 15px; height: 15px; fill: var(--blue); }
  .front-brand {
    position: absolute; right: 40px; top: 44px;
    display: flex; align-items: center; gap: 10px;
    color: var(--blue); font-size: 24px; font-weight: 400;
  }
  .front-brand__dot { width: 16px; height: 16px; border-radius: 50%; background: var(--yellow); }
  .website {
    position: absolute; right: 26px; bottom: 58px;
    color: var(--white); font-size: 13px; font-weight: 400;
    transform: rotate(-17deg); transform-origin: right bottom;
  }
</style>
</head>
<body>
<div class="canvas">

  <section class="card card--back" aria-label="Rückseite">
    <p class="quote" style="margin:0">„Denke immer daran,<br>dass es nur eine wichtige Zeit gibt:<br>Heute!&nbsp;&nbsp; Hier!&nbsp;&nbsp; Jetzt!“<span class="quote__author">Emil Roth, Schriftsteller</span></p>
    <div class="brand">
      <span class="brand__name">KraftQuellen</span>
      <span class="brand__dot"></span>
    </div>
    <div class="brand__tagline">stressgelassen • leben • arbeiten</div>
    <div class="benefits">Burnout vermeiden<span class="sep">•</span>Leistungsfähig bleiben<span class="sep">•</span>Gesund leben</div>
  </section>

  <section class="card card--front" aria-label="Vorderseite">
    <svg class="waves" viewBox="0 0 560 320" preserveAspectRatio="none" aria-hidden="true">
      <path d="M0 290 C 200 300, 380 240, 560 140 L560 320 L0 320 Z" fill="var(--yellow)"/>
      <path d="M0 305 C 200 318, 380 260, 560 160 L560 320 L0 320 Z" fill="var(--white)"/>
      <path d="M190 320 C 330 300, 450 240, 560 172 L560 320 Z" fill="var(--blue)"/>
    </svg>
    <div class="front-brand"><span>KraftQuellen</span><span class="front-brand__dot"></span></div>
    <div class="person">
      <h1 class="person__name">Jana Wellhof</h1>
      <div class="person__offer">Seminare • Coaching<br>für den gelassenen Umgang mit Stress</div>
    </div>
    <div class="credentials">Heilpraktikerin für Psychotherapie<br>Gesundheitscoach nach Prof. Lindner</div>
    <div class="contact">
      <div class="contact__row">
        <svg class="contact__icon" viewBox="0 0 24 24" aria-hidden="true"><path d="M6.6 10.8a15 15 0 0 0 6.6 6.6l2.2-2.2a1 1 0 0 1 1-.25 11.4 11.4 0 0 0 3.6.57 1 1 0 0 1 1 1V20a1 1 0 0 1-1 1A17 17 0 0 1 3 4a1 1 0 0 1 1-1h3.5a1 1 0 0 1 1 1c0 1.25.2 2.45.57 3.57a1 1 0 0 1-.25 1z"/></svg>
        <span>040 / 12 34 56 78</span>
      </div>
      <div class="contact__row">
        <svg class="contact__icon" viewBox="0 0 24 24" aria-hidden="true"><path d="M2 5h20v14H2z M3 6l9 7 9-7" fill="none" stroke="var(--blue)" stroke-width="2"/></svg>
        <span>starten@kraftquellen-beispiel.de</span>
      </div>
    </div>
    <div class="website">www.kraftquellen-beispiel.de</div>
  </section>

</div>
</body>
</html>
```